Boutique winery needs new wine label

mas Verlon is a boutique wine company based in the Clare Valley of South Australia. We are an established brand, best known for our Riesling and Grenache. We plan to launch a new sub brand called Le Doux mas and require a new label that is different from the others we use. It will be used on small batch Riesling and should have a rustic but quality feel. Attached is a small image of the house where the winery is based. The label should incorporate a hand drawn sketch of the house.
Target Market(s)
High end wine consumers with an interest in Riesling
Requirements
Must have
- hand drawn sketch of the house
- the name of the wine Le Doux mas present on the front label
- Vintage (2018) and region (Clare Valley) present on the front label
- Minimal use of colour on the label but would look at embellishments such as gold foil
Nice to have
- A clean, simple style of label, preferably with white background
- Le Doux mas written in script style
Should not have
- mas Verlon written on the front label
- the current mas Verlon logo

```html
<!DOCTYPE html>
<html lang="en">
<head>
<meta charset="utf-8">
<title>Le Doux mas – Wine Label</title>
<link href="https://fonts.googleapis.com/css2?family=Fondamento&family=Della+Respira&display=swap" rel="stylesheet">
<style>
  :root {
    --paper: #ffffff;
    --label-dark: #0f140d;
    --gold-light: #fbe68c;
    --gold-mid: #eec24a;
    --gold-deep: #b57a2c;
    --gold-text: #f2c85a;
    --sketch-light: #b9b9b9;
    --sketch-dark: #3a3a3a;
  }
  * { margin: 0; padding: 0; box-sizing: border-box; }
  html, body {
    width: 1134px;
    height: 1200px;
    overflow: hidden;
    background: var(--paper);
  }
  .canvas {
    position: relative;
    width: 1134px;
    height: 1200px;
  }
  .label-frame {
    position: absolute;
    left: 135px;
    top: 124px;
    width: 872px;
    height: 910px;
    padding: 15px;
    background: linear-gradient(90deg,
      var(--gold-mid) 0%, var(--gold-light) 22%, var(--gold-deep) 45%,
      var(--gold-mid) 65%, var(--gold-light) 82%, var(--gold-mid) 100%);
  }
  .label-face {
    position: relative;
    width: 100%;
    height: 100%;
    background: var(--label-dark);
  }
  .wine-name {
    position: absolute;
    left: 0;
    right: 0;
    top: 62px;
    text-align: center;
    font-family: "Fondamento", cursive;
    font-size: 112px;
    line-height: 1;
    color: var(--gold-text);
    background: linear-gradient(180deg, var(--gold-light) 10%, var(--gold-mid) 55%, var(--gold-deep) 100%);
    -webkit-background-clip: text;
    background-clip: text;
    -webkit-text-fill-color: transparent;
    filter: drop-shadow(0 0 6px rgba(0,0,0,0.8));
  }
  .house-frame {
    position: absolute;
    left: 159px;
    top: 254px;
    width: 525px;
    height: 329px;
    padding: 4px;
    background: linear-gradient(90deg, var(--gold-mid), var(--gold-light) 30%, var(--gold-deep) 55%, var(--gold-light) 80%, var(--gold-mid));
  }
  .house-sketch {
    width: 100%;
    height: 100%;
    background: var(--label-dark);
  }
  .details {
    position: absolute;
    left: 0;
    right: 0;
    top: 678px;
    text-align: center;
    font-family: "Della Respira", serif;
    font-size: 50px;
    line-height: 88px;
    letter-spacing: 3px;
    color: var(--gold-text);
  }
</style>
</head>
<body>
<div class="canvas">
  <div class="label-frame">
    <div class="label-face">
      <h1 class="wine-name">Le Doux mas</h1>
      <div class="house-frame">
        <svg class="house-sketch" role="img" aria-label="Hand drawn sketch of the winery house, a two-storey stone home covered in vines" viewBox="0 0 517 321" preserveAspectRatio="none">
          <defs>
            <linearGradient id="sketchTone" x1="0" y1="0" x2="0" y2="1">
              <stop offset="0" stop-color="var(--sketch-light)"/>
              <stop offset="1" stop-color="var(--sketch-dark)"/>
            </linearGradient>
          </defs>
          <rect x="0" y="40" width="517" height="281" fill="url(#sketchTone)"/>
        </svg>
      </div>
      <p class="details">Vintage 2018<br>Clare Valley</p>
    </div>
  </div>
</div>
</body>
</html>
```